Create the artwork for Velvetharbor's debut album, 'Where Rivers Bend Slowly'!

We are a cinematic pop/jazz quartet from Oslo/London looking for someone to create the artwork for our debutalbum, 'Where Rivers Bend Slowly'. This is a project we are incredibly proud of, and we are looking for the perfect artwork to complement our music.

We want the artwork to convey the organic feel of our sound, yet be eye-catching with bright colours. Attached are several examples for inspiration. The title of the album, 'Where Rivers Bend Slowly', should be an inspiration for the design in a subtle/abstract way. Think out of the box here, we are not looking for a hundred solar system designs.

You can find an album teaser here for inspiration: https://audiostreamhub.example/velvetharbormusic/album-teaser

This is our webpage: velvetharbormusic.example

Excited to see what you come up with and to work with some brilliant creatives !

Much love,

Velvetharbor
Updates

Everyone, thanks for your effort and great designs! We're discussing right now and will get back to you with feedback and suggested edits very shortly. Thanks for your patience! Much love, Velvetharbor

Requirements
Must have
• Ready-to-print high-res files in standard CD Cover format
• Artwork ready for digital release on tunewave, Songvault, and social media channels
Nice to have
• Would love to have smaller extensions of the artwork (pattern or pieces of art in same theme) to use on webpage/social media channels.

```html
<!DOCTYPE html>
<html lang="en">
<head>
<meta charset="utf-8">
<title>Velvetharbor – Where Rivers Bend Slowly – Artwork Set</title>
<link rel="stylesheet" href="https://fonts.googleapis.com/css2?family=Courier+Prime:wght@400;700&family=Reenie+Beanie&display=swap">
<style>
  :root {
    --page: #ffffff;
    --sky: #f1f1f1;
    --haze: #c9c9c9;
    --mid: #6d6d6d;
    --ground: #3a3a3a;
    --deep: #232323;
    --ink-light: #f4f4f4;
    --ink-dark: #1c1c1c;
    --accent-green: #7cff3a;
    --accent-green-dark: #2f7d12;
    --accent-violet: #b06cff;
    --accent-cyan: #4fd8ff;
    --frame: #555555;
  }
  * { box-sizing: border-box; margin: 0; padding: 0; }
  html, body {
    width: 1200px; height: 600px; overflow: hidden;
    background: var(--page);
    font-family: "Courier Prime", "Courier New", monospace;
  }
  .board { position: relative; width: 1200px; height: 600px; }

  .artwork { position: absolute; overflow: hidden; }
  .artwork__photo { position: absolute; inset: 0; }
  .photo--landscape {
    background:
      radial-gradient(ellipse 22% 18% at 78% 46%, rgba(176,108,255,.55), rgba(79,216,255,.35) 45%, rgba(124,255,58,.2) 70%, transparent 100%),
      radial-gradient(ellipse 30% 38% at 70% 30%, rgba(20,20,20,.85), transparent 75%),
      linear-gradient(180deg, var(--sky) 0%, var(--haze) 38%, var(--mid) 48%, var(--ground) 62%, var(--deep) 100%);
  }
  .photo--light {
    background:
      radial-gradient(ellipse 25% 40% at 100% 30%, rgba(40,40,40,.8), transparent 80%),
      linear-gradient(180deg, #fbfbfb 0%, #e4e4e4 55%, #9a9a9a 72%, #5b5b5b 100%);
  }

  .band-name {
    font-family: "Reenie Beanie", "Comic Sans MS", cursive;
    font-weight: 400;
    white-space: nowrap;
    line-height: 1;
  }
  .album-title { white-space: nowrap; font-weight: 400; }
  .album-title .word-shift { color: var(--accent-green); }
  .album-title .line-2 { display: block; }

  /* main cover */
  .cover-main { left: 0; top: 0; width: 594px; height: 600px; }
  .cover-main .band-name {
    position: absolute; left: 240px; top: 440px;
    font-size: 76px; color: var(--ink-light);
  }
  .cover-main .album-title {
    position: absolute; left: 298px; top: 512px;
    font-size: 19px; line-height: 18px; color: var(--ink-light);
  }
  .cover-main .album-title .line-2 { padding-left: 68px; }

  /* vinyl sleeve, flat */
  .sleeve { left: 682px; top: 60px; width: 286px; height: 286px; border: 1px solid var(--frame); }
  .sleeve .band-name {
    position: absolute; left: 14px; top: 92px;
    font-size: 30px; color: var(--ink-dark);
  }

  /* CD front */
  .cd-front { left: 682px; top: 374px; width: 180px; height: 184px; }
  .cd-front .band-title {
    position: absolute; left: 16px; top: 19px;
    font-family: "Courier Prime", "Courier New", monospace;
    font-size: 14px; font-weight: 700; line-height: 12px; letter-spacing: 1px;
    color: var(--ink-light);
  }
  .cd-front .album-title {
    position: absolute; left: 28px; top: 48px;
    font-size: 7px; line-height: 7px; color: var(--ink-light);
  }
  .cd-front .album-title .line-2 { padding-left: 18px; }

  /* CD back */
  .cd-back { left: 885px; top: 374px; width: 188px; height: 184px; }
  .cd-back .band-name {
    position: absolute; left: 8px; top: 24px;
    font-size: 24px; color: var(--ink-dark);
  }
  .cd-back .album-title {
    position: absolute; left: 12px; top: 52px;
    font-size: 9px; line-height: 8px; color: var(--ink-dark);
  }
  .cd-back .album-title .word-shift { color: var(--accent-green-dark); }
  .cd-back .album-title .line-2 { padding-left: 24px; }
  .tracklist {
    position: absolute; left: 12px; top: 72px;
    list-style: none; font-size: 5px; line-height: 6.2px; color: var(--ink-dark);
  }
</style>
</head>
<body>
<main class="board">

  <section class="artwork cover-main">
    <div class="artwork__photo photo--landscape" role="img" aria-label="Glitched black and white photo of a woman in a field under a pale sky, with a rainbow butterfly wing over her face"></div>
    <h1 class="band-name">Velvetharbor</h1>
    <p class="album-title">Where <span class="word-shift">Rivers</span><span class="line-2">Bend <span class="word-shift">Slowly</span></span></p>
  </section>

  <section class="artwork sleeve">
    <div class="artwork__photo photo--landscape" role="img" aria-label="Vinyl sleeve version of the glitched field portrait with rainbow butterfly wing"></div>
    <h2 class="band-name">Velvetharbor</h2>
  </section>

  <section class="artwork cd-front">
    <div class="artwork__photo photo--landscape" role="img" aria-label="Close crop of the glitched portrait with rainbow butterfly wing"></div>
    <h2 class="band-title">VELVET<br>HARBOR</h2>
    <p class="album-title">Where <span class="word-shift">Rivers</span><span class="line-2">Bend <span class="word-shift">Slowly</span></span></p>
  </section>

  <section class="artwork cd-back">
    <div class="artwork__photo photo--light" role="img" aria-label="Pale sky and horizon from the glitched field photo"></div>
    <h2 class="band-name">Velvetharbor</h2>
    <p class="album-title">Where <span class="word-shift">Rivers</span><span class="line-2">Bend <span class="word-shift">Slowly</span></span></p>
    <ol class="tracklist">
      <li>Track One</li><li>Track Two</li><li>Track Three</li><li>Track Four</li><li>Track Five</li>
      <li>Track Six</li><li>Track Seven</li><li>Track Eight</li><li>Track Nine</li><li>Track Ten</li>
    </ol>
  </section>

</main>
</body>
</html>
```